Branding for Clear Current Honours program collateral

The Clear Current Honours, hosted by the Flowline Sector Council, are an annual awards program to recognise excellence in the Australian water industry. The awards presentation ceremony is held over a formal luncheon, with a MC and Keynote Speaker. The awards event is a premium experience for business professionals that work in the work sector. It is a corporate business luncheon with management level professionals in attendance. We are seeking branding design elements that we can use on all awards collateral including the website, printed invitation, event program, social media posts etc. The Clear Current Honours are well known in the industry and recognised by its logo and corporate colours (attached). We would like these incorporated into the design.

Target Market(s)

business professionals

Industry/Entity Type

Water Company

Requirements
Must have
• event logo, corporate colours

```html
<!DOCTYPE html>
<html lang="en">
<head>
<meta charset="utf-8">
<title>Clear Current Honours</title>
<link rel="stylesheet" href="https://fonts.googleapis.com/css2?family=Montserrat:wght@400;500;600&display=swap">
<style>
  :root {
    --coral: #fd8369;
    --sand: #d9a08e;
    --sage: #b5bcaa;
    --aqua: #6ff6f6;
    --orange: #ff8000;
    --magenta: #ff00ff;
    --cyan: #00e1ff;
    --lime: #80ff00;
    --white: #ffffff;
  }
  * { margin: 0; padding: 0; box-sizing: border-box; }
  html, body { width: 1200px; height: 842px; overflow: hidden; }
  body { font-family: "Montserrat", sans-serif; }

  .card {
    position: relative;
    width: 1200px;
    height: 842px;
    overflow: hidden;
    background: linear-gradient(90deg, var(--coral) 0%, var(--coral) 8%, var(--sand) 50%, var(--sage) 68%, var(--aqua) 100%);
    color: var(--white);
  }

  .title-frame {
    position: absolute;
    left: 61px;
    top: 110px;
    width: 666px;
    height: 114px;
  }
  .title-frame svg { position: absolute; inset: 0; }

  .event-name {
    position: absolute;
    left: 61px;
    width: 666px;
    top: 128px;
    text-align: center;
    font-weight: 600;
    font-size: 56px;
    letter-spacing: 1.5px;
    line-height: 1;
  }
  .event-kind {
    position: absolute;
    left: 61px;
    width: 666px;
    top: 211px;
    text-align: center;
    font-weight: 600;
    font-size: 20px;
    letter-spacing: 5px;
  }
  .event-region {
    position: absolute;
    left: 61px;
    width: 666px;
    top: 256px;
    text-align: center;
    font-weight: 400;
    font-size: 17px;
    letter-spacing: 4px;
  }

  .host {
    position: absolute;
    left: 86px;
    width: 220px;
    top: 600px;
    text-align: center;
  }
  .host-mark {
    display: block;
    margin: 0 auto 34px;
  }
  .host-name {
    font-weight: 500;
    font-size: 23px;
    line-height: 1.35;
  }

  .facet-art {
    position: absolute;
    left: 552px;
    top: 0;
    width: 648px;
    height: 842px;
    background:
      radial-gradient(circle at 55% 25%, var(--orange) 0%, rgba(255,128,0,0) 45%),
      radial-gradient(circle at 45% 60%, var(--magenta) 0%, rgba(255,0,255,0) 40%),
      radial-gradient(circle at 85% 65%, var(--cyan) 0%, rgba(0,225,255,0) 45%),
      radial-gradient(circle at 65% 90%, var(--magenta) 0%, rgba(255,0,255,0) 35%),
      linear-gradient(160deg, var(--orange) 0%, var(--cyan) 100%);
    clip-path: polygon(36% 0%, 100% 0%, 100% 100%, 68% 100%, 50% 90%, 40% 80%, 30% 68%, 20% 60%, 0% 42%, 12% 35%, 30% 25%, 45% 17%);
    opacity: 0.9;
  }
</style>
</head>
<body>
  <main class="card">
    <div class="title-frame" aria-hidden="true">
      <svg width="666" height="114" viewBox="0 0 666 114">
        <polyline points="165,111 3,111 3,3 663,3 663,111 500,111" fill="none" stroke="var(--white)" stroke-width="5.6"/>
      </svg>
    </div>
    <h1 class="event-name">Clear Current</h1>
    <p class="event-kind">HONOURS</p>
    <p class="event-region">SOUTH AUSTRALIA</p>

    <div class="host">
      <svg class="host-mark" width="70" height="70" viewBox="0 0 70 70" aria-hidden="true">
        <circle cx="35" cy="35" r="30" fill="none" stroke="var(--white)" stroke-width="7"/>
      </svg>
      <p class="host-name">Flowline Sector<br>Council</p>
    </div>

    <div class="facet-art" role="img" aria-label="Abstract isometric cube pattern in orange, magenta, cyan and lime"></div>
  </main>
</body>
</html>
```